Dental Practice Billboard Design

We are a newer dental practice in need of a simple but appealing billboard for our growing dental practice to attract new patients. The practice is owned by husband and wife dentists and is family friendly in a small town in Kentucky. We try to be very friendly and caring to our patients. Would prefer a blue background for the billboard and our tooth logo to be prominent. We are partial to the Patua One font used in the image below but please feel free to tweak it as you deem necessary. The shape of the uppercase D and lowercase g are why we like that font, so fonts with a similarly shaped “D” and “g” would work as well. Please include our phone number (606) 847-3962. Please see our website Harlowfamilydentistry.com for more info on the practice if needed. Thank you! Looking forward to seeing your creation.
Updates

The dimensions will be 12ft x 24ft (3.6576m x 7.3152m). Apologies for not including this in the original prompt. Thank you all for your submissions.

Industry/Entity Type

Dental

Font styles to use
Other font styles liked:
• Patua One

Colors
0054AA
0677BA
7BADD7
CADEEF
E8F1F8
0094D4
00A9DD
6FCCEA
C7EBF8
E9F6FB
00AB8E
00BBA5
67D7C9
C6EFE9
E9F9F6
59FF00
82FF00
B8FF75
E3FFCB
F4FFEA

Requirements
Must have
• Phone number, website, Logo, Practice name “Harlow Family Dentistry”
Should not have
• A tagline or slogan

```html
<!DOCTYPE html>
<html lang="en">
<head>
<meta charset="utf-8">
<title>Harlow Family Dentistry Billboard</title>
<link rel="stylesheet" href="https://fonts.googleapis.com/css2?family=Patua+One&family=Bitter:wght@700&family=Fira+Sans:wght@600&display=swap">
<style>
  :root {
    --page-bg: #eef2f7;
    --board-blue: #243a87;
    --leaf-green: #6ab843;
    --tick-green: #1f5a2e;
    --sky-blue: #5bbfe0;
    --white: #ffffff;
  }
  * { margin: 0; padding: 0; box-sizing: border-box; }
  html, body { width: 1200px; height: 1000px; overflow: hidden; background: var(--page-bg); }
  .canvas { position: relative; width: 1200px; height: 1000px; }
  .billboard-scale {
    position: absolute; left: 0; top: 198px;
    width: 1014px; height: 510px;
    transform: scale(1.1834); transform-origin: 0 0;
  }
  .billboard {
    position: relative; width: 1014px; height: 510px;
    background: var(--board-blue); overflow: hidden;
  }
  .brand-mark {
    position: absolute; left: 150px; top: 52px;
    width: 180px; height: 180px; border-radius: 50%;
    background: var(--leaf-green);
  }
  .practice-name { color: var(--white); font-family: "Patua One", serif; font-weight: 400; }
  .practice-name__main {
    position: absolute; left: 0; top: 22px; width: 1014px; padding-left: 392px;
    font-size: 122px; line-height: 1; white-space: nowrap;
  }
  .practice-name__sub {
    position: absolute; left: 0; top: 140px; width: 1014px; padding-left: 386px;
    font-size: 56px; line-height: 1; white-space: nowrap;
  }
  .name-rule {
    position: absolute; left: 330px; top: 210px; width: 588px; height: 1px;
    background: linear-gradient(90deg, transparent, rgba(255,255,255,0.8) 20%, rgba(255,255,255,0.8) 80%, transparent);
  }
  .website {
    position: absolute; left: 330px; top: 220px; width: 588px; text-align: center;
    font-family: "Bitter", serif; font-weight: 700; font-size: 23px; line-height: 30px;
    color: var(--leaf-green);
  }
  .services-frame {
    position: absolute; left: 33px; top: 288px; width: 948px; height: 79px;
    border: 2px solid var(--white);
  }
  .services-title {
    position: absolute; left: 0; top: 268px; width: 1014px; text-align: center;
    font-family: "Bitter", serif; font-weight: 700; font-size: 23px; line-height: 34px;
    color: var(--leaf-green);
  }
  .services-title span { background: var(--board-blue); padding: 0 10px; }
  .services-list {
    position: absolute; left: 51px; top: 300px; width: 912px; height: 98px;
    background: var(--leaf-green); list-style: none;
    display: grid; grid-template-columns: 240px 248px 218px 190px; grid-template-rows: repeat(3, 30px);
    grid-auto-flow: column; padding: 5px 0 0 12px;
    font-family: "Bitter", serif; font-weight: 700; font-size: 18px; color: var(--white);
  }
  .service { display: flex; align-items: center; gap: 4px; white-space: nowrap; }
  .service svg { width: 12px; height: 14px; flex: none; }
  .call-line {
    position: absolute; left: 0; top: 412px; width: 1014px; text-align: center;
    font-family: "Fira Sans", sans-serif; font-weight: 600; font-size: 58px; line-height: 1;
    white-space: nowrap;
  }
  .call-line__prompt { color: var(--sky-blue); }
  .call-line__phone { color: var(--white); }
</style>
</head>
<body>
<div class="canvas">
  <div class="billboard-scale">
    <section class="billboard">
      <div class="brand-mark"></div>
      <h1 class="practice-name">
        <span class="practice-name__main">Harlow</span>
        <span class="practice-name__sub">Family Dentistry</span>
      </h1>
      <div class="name-rule"></div>
      <p class="website">Harlowfamilydentistry.com</p>
      <div class="services-frame"></div>
      <h2 class="services-title"><span>Our Services</span></h2>
      <ul class="services-list">
        <li class="service"><svg viewBox="0 0 13 15"><path d="M2 8 L5.5 12 L11 2" fill="none" stroke="#1f5a2e" stroke-width="2"/></svg>Crowns</li>
        <li class="service"><svg viewBox="0 0 13 15"><path d="M2 8 L5.5 12 L11 2" fill="none" stroke="#1f5a2e" stroke-width="2"/></svg>Root Canals</li>
        <li class="service"><svg viewBox="0 0 13 15"><path d="M2 8 L5.5 12 L11 2" fill="none" stroke="#1f5a2e" stroke-width="2"/></svg>Extractions</li>
        <li class="service"><svg viewBox="0 0 13 15"><path d="M2 8 L5.5 12 L11 2" fill="none" stroke="#1f5a2e" stroke-width="2"/></svg>Implants</li>
        <li class="service"><svg viewBox="0 0 13 15"><path d="M2 8 L5.5 12 L11 2" fill="none" stroke="#1f5a2e" stroke-width="2"/></svg>Bridges</li>
        <li class="service"><svg viewBox="0 0 13 15"><path d="M2 8 L5.5 12 L11 2" fill="none" stroke="#1f5a2e" stroke-width="2"/></svg>Clear Aligner</li>
        <li class="service"><svg viewBox="0 0 13 15"><path d="M2 8 L5.5 12 L11 2" fill="none" stroke="#1f5a2e" stroke-width="2"/></svg>Veneers</li>
        <li class="service"><svg viewBox="0 0 13 15"><path d="M2 8 L5.5 12 L11 2" fill="none" stroke="#1f5a2e" stroke-width="2"/></svg>Whitening</li>
        <li class="service"><svg viewBox="0 0 13 15"><path d="M2 8 L5.5 12 L11 2" fill="none" stroke="#1f5a2e" stroke-width="2"/></svg>Fillings</li>
        <li class="service"><svg viewBox="0 0 13 15"><path d="M2 8 L5.5 12 L11 2" fill="none" stroke="#1f5a2e" stroke-width="2"/></svg>Cleanings</li>
        <li class="service"><svg viewBox="0 0 13 15"><path d="M2 8 L5.5 12 L11 2" fill="none" stroke="#1f5a2e" stroke-width="2"/></svg>Dentures</li>
        <li class="service"><svg viewBox="0 0 13 15"><path d="M2 8 L5.5 12 L11 2" fill="none" stroke="#1f5a2e" stroke-width="2"/></svg>Overdentures</li>
      </ul>
      <p class="call-line"><span class="call-line__prompt">CALL TODAY!</span> <span class="call-line__phone">(606) 847-3962</span></p>
    </section>
  </div>
</div>
</body>
</html>
```